PSD website for property company

Please read the brief thoroughly.

We are looking for a new website for a property group that does property acquisitions, property development and property management.
They buy, build and lease core inner city industrial assets in Sydney, Australia.
They also invest in residential developments.

Site menu
- Home page
- Property – sub menus include – Leasing ; Projects ; Investments ; Property Management
- Capital and finance
- About
- Contact

They like this website
https://www.verlo.com.au/

They want the site to be clean, modern and bold.
They like few colors, even black and white is OK to submit

They have a logo and style guide and useable images here:
http://www.kumet.net/temp/PelorisWeb2019.zip
The zip file is also attached to this project.
We have supplied some images to give you an idea, but we will also require you to provide at least 3 extra images from stock photos.
Use your imagination.

I am expecting a lot of similar designs, so be aware the photos you choose will be really important.
They want really 3 good stock photos used and supplied without charge.
Please not too generic, I repeat the quality of the photos is important.
You may provide several photos (but not in multiple submissions please) and we will choose the best three to be provided.

The winner will be selected on a single home page design and required to provide;
All photos use in original format without charge
A second ‘standard page’ template design based on the winning home page design

```html
<!DOCTYPE html>
<html lang="en">
<head>
<meta charset="utf-8">
<title>Haldene — Standard Page</title>
<link rel="stylesheet" href="https://fonts.googleapis.com/css2?family=Arimo:ital,wght@0,400;0,500;0,700;1,400&family=Inter:wght@500;600&family=Poppins:wght@600&display=swap">
<style>
:root{
  --ink:#2b2b2b;
  --bar:#353535;
  --bar-bottom:#333333;
  --white:#ffffff;
  --footer-bg:#f4f9ef;
  --accent:#9db59b;
  --hero-dark:#2f3d46;
  --hero-sky:#3a97bd;
}
*{box-sizing:border-box;margin:0;padding:0}
html,body{width:1200px;height:2392px;overflow:hidden;background:var(--white)}
body{position:relative;font-family:"Arimo",Helvetica,Arial,sans-serif;color:var(--ink)}
.site-header{position:absolute;left:0;top:0;width:1200px;height:91px;background:var(--bar);color:var(--white)}
.nav-link{position:absolute;top:40px;font-family:"Inter",Arial,sans-serif;font-size:10.5px;font-weight:500;letter-spacing:1.6px;text-transform:uppercase;line-height:12px}
.nav-link .caret{display:inline-block;margin-left:6px;vertical-align:2px;width:0;height:0;border-left:4px solid transparent;border-right:4px solid transparent;border-top:4px solid var(--white)}
.brand{position:absolute;left:0;width:1200px;top:24px;text-align:center;font-family:"Inter",Arial,sans-serif;font-weight:600;font-size:36px;letter-spacing:8px;line-height:44px}
.hero{position:absolute;left:0;top:91px;width:1200px;height:292px;background:linear-gradient(110deg,var(--hero-dark) 0%,#3b4b55 40%,#3a7fa0 62%,var(--hero-sky) 100%)}
.page-title{position:absolute;left:229px;top:185px;font-family:"Poppins",Arial,sans-serif;font-weight:600;font-size:40px;color:var(--white);line-height:50px}
.content{position:absolute;left:229px;width:742px}
.heading{position:absolute;left:229px;font-family:"Inter",Arial,sans-serif;font-weight:600;font-size:25px;line-height:30px}
.intro{font-size:17.4px;line-height:26.7px}
.body-text{font-size:13.7px;line-height:20px}
.photo{position:absolute;left:229px;top:992px;width:739px;height:492px;background:linear-gradient(180deg,#dfe5e8 0%,#cfd6d8 55%,#bfc6c4 75%,#5d7a55 90%,#3f5a3a 100%)}
.caption{position:absolute;left:229px;width:739px;top:1499px;text-align:right;font-style:italic;font-size:11.8px;line-height:16px}
.back-top{position:absolute;left:1004px;top:2133px;width:54px;height:54px;background:var(--accent)}
.site-footer{position:absolute;left:0;top:2163px;width:1200px;height:163px;background:var(--footer-bg)}
.footer-nav{position:absolute;left:0;width:1200px;top:54px;text-align:center;font-size:12.2px;font-weight:500;line-height:14px}
.footer-nav span{margin:0 13px}
.social{position:absolute;left:553px;top:101px;display:flex;gap:20px}
.social span{display:block;width:14px;height:14px;border-radius:50%;background:var(--ink)}
.legal-bar{position:absolute;left:0;top:2326px;width:1200px;height:66px;background:var(--bar-bottom);color:var(--white);font-size:10.5px;line-height:12px}
.legal-left{position:absolute;left:38px;top:27px}
.legal-right{position:absolute;right:38px;top:27px;font-weight:500}
.legal-right svg{vertical-align:-1px;margin-right:4px}
</style>
</head>
<body>
<header class="site-header">
  <div class="nav-link" style="left:37px">Property<span class="caret"></span></div>
  <div class="nav-link" style="left:170px">Capital &amp; Finance</div>
  <div class="brand">HALDENE</div>
  <div class="nav-link" style="left:1013px">About</div>
  <div class="nav-link" style="left:1105px">Contact</div>
</header>

<section class="hero" role="img" aria-label="Looking up between dark glass office towers into a clear blue sky">
  <h1 class="page-title">Page Title</h1>
</section>

<h2 class="heading" style="top:467px">Heading</h2>
<p class="content intro" style="top:535px">Optional Intro Text - Lorem ipsum dolor sit amet, consectetur adipiscing elit, sed do eiusmod tempor incididunt ut labore et dolore magna aliqua. Ut enim ad minim veniam, quis nostrud exercitation ullamco laboris nisi ut aliquip ex ea commodo consequat. Duis aute irure dolor in reprehenderit in voluptate velit esse cillum dolore eu fugiat nulla pariatur. Excepteur sint occaecat cupidatat non proident, sunt in culpa qui officia deserunt mollit anim id est laborum.</p>
<p class="content body-text" style="top:702px">Standard Body Text - Lorem ipsum dolor sit amet, consectetur adipiscing elit, sed do eiusmod tempor incididunt ut labore et dolore magna aliqua. Ut enim ad minim veniam, quis nostrud exercitation ullamco laboris nisi ut aliquip ex ea commodo consequat. Duis aute irure dolor in reprehenderit in voluptate velit esse cillum dolore eu fugiat nulla pariatur. Excepteur sint occaecat cupidatat non proident, sunt in culpa qui officia deserunt mollit anim id est laborum.</p>
<p class="content body-text" style="top:802px">Lorem ipsum dolor sit amet, consectetur adipiscing elit, sed do eiusmod tempor incididunt ut labore et dolore magna aliqua. Ut enim ad minim veniam, quis nostrud exercitation ullamco laboris nisi ut aliquip ex ea commodo consequat. Duis aute irure dolor in reprehenderit in voluptate velit esse cillum dolore eu fugiat nulla pariatur. Excepteur sint occaecat cupidatat non proident, sunt in culpa qui officia deserunt mollit anim id est laborum.<br>Lorem ipsum dolor sit amet, consectetur adipiscing elit, sed do eiusmod tempor incididunt ut labore et dolore magna aliqua. Ut enim ad minim veniam, quis nostrud exercitation ullamco laboris nisi ut aliquip ex ea commodo consequat. Duis aute irure dolor in reprehenderit in voluptate velit esse cillum dolore eu fugiat nulla pariatur. Excepteur sint.</p>

<div class="photo" role="img" aria-label="Glass-roofed sky garden walkway overlooking city buildings, with planting below"></div>
<p class="caption">Image Description / Credit</p>

<p class="content body-text" style="top:1565px">Standard Body Text - Lorem ipsum dolor sit amet, consectetur adipiscing elit, sed do eiusmod tempor incididunt ut labore et dolore magna aliqua. Ut enim ad minim veniam, quis nostrud exercitation ullamco laboris nisi ut aliquip ex ea commodo consequat. Duis aute irure dolor in reprehenderit in voluptate velit esse cillum dolore eu fugiat nulla pariatur. Excepteur sint occaecat cupidatat non proident, sunt in culpa qui officia deserunt mollit anim id est laborum.</p>
<p class="content body-text" style="top:1665px">Lorem ipsum dolor sit amet, consectetur adipiscing elit, sed do eiusmod tempor incididunt ut labore et dolore magna aliqua. Ut enim ad minim veniam, quis nostrud exercitation ullamco laboris nisi ut aliquip ex ea commodo consequat. Duis aute irure dolor in reprehenderit in voluptate velit esse cillum dolore eu fugiat nulla pariatur. Excepteur sint occaecat cupidatat non proident, sunt in culpa qui officia deserunt mollit anim id est laborum.<br>Lorem ipsum dolor sit amet, consectetur adipiscing elit, sed do eiusmod tempor incididunt ut labore et dolore magna aliqua. Ut enim ad minim veniam, quis nostrud exercitation ullamco laboris nisi ut.</p>

<h2 class="heading" style="top:1835px">Heading</h2>
<p class="content body-text" style="top:1903px">Standard Body Text - Lorem ipsum dolor sit amet, consectetur adipiscing elit, sed do eiusmod tempor incididunt ut labore et dolore magna aliqua. Ut enim ad minim veniam, quis nostrud exercitation ullamco laboris nisi ut aliquip ex ea commodo consequat. Duis aute irure dolor in reprehenderit in voluptate velit esse cillum dolore eu fugiat nulla pariatur. Excepteur sint occaecat cupidatat non proident, sunt in culpa qui officia deserunt mollit anim id est laborum.</p>
<p class="content body-text" style="top:2003px">Lorem ipsum dolor sit amet, consectetur adipiscing elit, sed do eiusmod tempor incididunt ut labore et dolore magna aliqua. Ut enim ad minim veniam, quis nostrud exercitation ullamco laboris nisi ut aliquip ex ea commodo consequat. Duis aute irure dolor in reprehenderit in voluptate velit esse cillum dolore eu fugiat nulla pariatur. Excepteur sint occaecat cupidatat non proident, sunt in culpa qui officia deserunt mollit anim id est laborum.</p>

<footer class="site-footer">
  <nav class="footer-nav"><span>About</span><span>Contact</span><span>Property</span><span>Capital &amp; Finance</span></nav>
  <div class="social"><span aria-label="Social link"></span><span aria-label="Social link"></span><span aria-label="Social link"></span></div>
</footer>

<div class="back-top" aria-label="Back to top">
  <svg width="54" height="54" viewBox="0 0 54 54"><polyline points="20,30 27,23 34,30" fill="none" stroke="#2b2b2b" stroke-width="2.4"/></svg>
</div>

<div class="legal-bar">
  <div class="legal-left">© Copyright 2018 - 2019 &nbsp;|&nbsp;&nbsp; All Rights Reserved</div>
  <div class="legal-right"><svg width="9" height="9" viewBox="0 0 10 10"><path d="M2 1 L4 1 L5 3.5 L3.8 4.5 Q5 6.5 6 6.8 L7 5.6 L9.5 6.5 L9.5 8.5 Q9 9.5 7.5 9.3 Q1 8 0.7 2.5 Q0.7 1 2 1Z" fill="#fff"/></svg>(02) 5550 4127 &nbsp;|&nbsp; CONTACT / MEDIA INQUIRIES</div>
</div>
</body>
</html>
```